KV Group

We need a new website for our company and since we had a very good work done for our logo in this site, we're back for the entire job.

Our company name is Marlowe Capital Group. We're adding files of examples of what we have done today. In my opinion we need a more attention lock in the site but yet financial simple work.

Our files (attached) will let you know what we have so far. We need a complete change but the colours should be the same, however you can change them not running away to far from the original, and of course matching with the logo.

We need examples for 3 kind of layouts.

- A HOME welcome layout
- An internal Layout with sidebar
- And internal Layout wide

We can buy image licenses if needed for assets.
Actually there are 5 slide images placed on the Welcome HOME, we need those there, but you can improve with better images to match the new website!!!

Target Market(s)

Clients looking for financial advisers, tax and funds specialist, currency advisers

Industry/Entity Type

Financial

Requirements
Must have
• all the fonts must be in accordance with the financial market sites........the welcome home page must be precise, neat and information accurate........the menu should be elegant........main focus on the Home page, should be also the PRIVATE ACCESS box log in.......

```html
<!DOCTYPE html>
<html lang="en">
<head>
<meta charset="utf-8">
<title>Marlowe Capital Group — About Us</title>
<link rel="stylesheet" href="https://fonts.googleapis.com/css2?family=Open+Sans:wght@300;400;600;700&display=swap">
<style>
:root{
  --page-bg:#e8e4de;
  --panel:#f0ede8;
  --header:#f1eee9;
  --brown-dark:#3a2414;
  --brown:#5b3f29;
  --orange:#f07f22;
  --ink:#2c2c2c;
  --muted:#8a8580;
  --rule:#d6d2cc;
  --link:#efe9e2;
  --badge:#cfcac3;
}
*{margin:0;padding:0;box-sizing:border-box}
html,body{width:1047px;height:1200px;overflow:hidden}
body{font-family:"Open Sans",Arial,sans-serif;background:var(--page-bg);position:relative;color:var(--ink)}
.hero-photo{position:absolute;left:0;top:0;width:1047px;height:403px;
  background:linear-gradient(90deg,#2b2a26 0%,#4a4a44 25%,#3a3833 50%,#55544e 75%,#2e2d29 100%)}
.hero-photo::after{content:"";position:absolute;inset:0;background:linear-gradient(180deg,rgba(0,0,0,.15),rgba(0,0,0,.35))}
.header{position:absolute;left:75px;top:0;width:897px;height:123px;background:var(--header);border-radius:0 0 4px 4px;box-shadow:0 2px 6px rgba(0,0,0,.3)}
.brand{position:absolute;left:14px;top:66px;display:flex;align-items:center;gap:8px;font-size:19px;font-weight:600;color:#1d1d1d;letter-spacing:.5px}
.brand-mark{width:22px;height:22px;background:var(--orange)}
.utility{position:absolute;left:660px;top:0;width:230px;height:30px;background:var(--brown-dark);border-radius:0 0 0 4px;display:flex;align-items:center;font-size:8.5px;color:#fff;font-weight:600}
.utility span{display:flex;align-items:center;gap:5px}
.utility .apply{margin-left:34px}
.utility .contact{margin-left:22px}
.search{position:absolute;right:0;top:0;width:21px;height:30px;background:var(--orange);display:flex;align-items:center;justify-content:center}
.nav{position:absolute;left:376px;top:77px;display:flex;font-size:11.6px;color:#2a2a2a;white-space:nowrap}
.nav li{list-style:none;display:flex;align-items:center;margin-right:13px}
.nav li:last-child{margin-right:0}
.nav .caret{width:0;height:0;border-left:3.5px solid transparent;border-right:3.5px solid transparent;border-top:4px solid var(--orange);margin-left:6px}
.tagline{position:absolute;background:rgba(40,36,32,.82);color:#eee;font-weight:400;font-size:20.5px;text-align:center;line-height:42px;white-space:nowrap}
.tag-1{left:322px;top:153px;width:440px}
.tag-2{left:262px;top:200px;width:549px}
.panel{position:absolute;left:77px;top:270px;width:896px;height:622px;background:var(--panel);border-radius:4px 4px 0 0;box-shadow:0 0 8px rgba(0,0,0,.15)}
.panel h1{position:absolute;left:18px;top:22px;font-size:22.5px;font-weight:300;color:#333}
.panel .rule{position:absolute;left:18px;top:59px;width:847px;border-top:1px solid var(--rule)}
.photo{position:absolute;border:2px solid #fff;border-radius:3px;box-shadow:0 0 3px rgba(0,0,0,.2)}
.photo-coins{left:25px;top:89px;width:180px;height:125px;background:linear-gradient(135deg,#e9eef3 0%,#cfd6dc 40%,#c9a44e 65%,#8f6f2c 100%)}
.photo-paper{left:672px;top:297px;width:179px;height:126px;background:linear-gradient(135deg,#a55a4a 0%,#d49a7e 40%,#e9c7ad 60%,#3b2320 100%)}
.copy{position:absolute;font-size:9.4px;line-height:18.8px;color:var(--muted)}
.copy-about{left:237px;top:88px;width:623px}
.panel h2{position:absolute;left:18px;top:267px;font-size:17.5px;font-weight:300;color:#333}
.copy-second{left:19px;top:298px;width:623px}
.verified{position:absolute;left:0;top:522px;width:896px;text-align:center;font-size:13px;font-weight:700;color:#555;letter-spacing:.3px}
.badge{position:absolute}
.footer{position:absolute;left:0;top:892px;width:1047px;height:261px;background:var(--brown)}
.footer-col{position:absolute;top:26px}
.footer-col h3{font-size:15px;font-weight:400;color:var(--orange);margin-bottom:13px;white-space:nowrap}
.footer-col li{list-style:none;font-size:11.4px;color:var(--link);line-height:18.1px;white-space:nowrap}
.bottom-bar{position:absolute;left:0;top:1153px;width:1047px;height:47px;background:var(--brown-dark)}
</style>
</head>
<body>
<div class="hero-photo" role="img" aria-label="Dusk aerial view of a dense city skyline"></div>

<header class="header">
  <div class="brand"><span class="brand-mark"></span>Marlowe Capital Group</div>
  <div class="utility">
    <span class="apply"><svg width="9" height="9" viewBox="0 0 9 9"><path d="M2 0v7h7M0 2h7v7" fill="none" stroke="#fff" stroke-width="1"/></svg>APPLY NOW</span>
    <span class="contact"><svg width="9" height="10" viewBox="0 0 9 10"><circle cx="4.5" cy="3" r="2.5" fill="#fff"/><path d="M0 10c0-3 2-4.5 4.5-4.5S9 7 9 10z" fill="#fff"/></svg>CONTACT US</span>
    <div class="search"><svg width="11" height="11" viewBox="0 0 11 11"><circle cx="4.3" cy="4.3" r="3.2" fill="none" stroke="#fff" stroke-width="1.6"/><path d="M6.8 6.8l3.4 3.4" stroke="#fff" stroke-width="1.8"/></svg></div>
  </div>
  <ul class="nav">
    <li>ABOUT US<span class="caret"></span></li>
    <li>INVESTMENTS<span class="caret"></span></li>
    <li>FUNDS<span class="caret"></span></li>
    <li>BROKERAGE<span class="caret"></span></li>
    <li>EXCHANGE<span class="caret"></span></li>
    <li>ACCOUNTS</li>
  </ul>
</header>

<div class="tagline tag-1">Lorem Ipsum Lorem Ipsum Lorem Ipsum</div>
<div class="tagline tag-2">Lorem Ipsum Lorem Ipsum Lorem Ipsum Lorem Ipsu</div>

<main class="panel">
  <h1>About Us</h1>
  <div class="rule"></div>
  <div class="photo photo-coins" role="img" aria-label="Stacks of gold coins on financial papers"></div>
  <p class="copy copy-about">Lorem Ipsum is simply dummy text of the printing and typesetting industry. Lorem Ipsum has Lorem Ipsum is simply dummy text of the printing and typesetting industry. Lorem Ipsum has Lorem Ipsum is simply dummy text of the printing and typesetting industry. Lorem Ipsum has Lorem Ipsum is simply dummy text of the printing and typesetting industry. Lorem Ipsum has Lorem Ipsum is simply dummy text of the printing and typesetting industry. Lorem Ipsum has Lorem Ipsum is simply dummy text of the printing and typesetting industry. Lorem Ipsum has Lorem Ipsum is simply dummy text of the printing and typesetting industry. Lorem Ipsum has Lorem Ipsum is simply dummy text of the printing and typesetting industry. Lorem Ipsum has Lorem Ipsum is simply dummy text of the printing and typesetting industry. Lorem Ipsum has</p>
  <h2>Lorem Ipsum</h2>
  <p class="copy copy-second">Lorem Ipsum is simply dummy text of the printing and typesetting industry. Lorem Ipsum has Lorem Ipsum is simply dummy text of the printing and typesetting industry. Lorem Ipsum has Lorem Ipsum is simply dummy text of the printing and typesetting industry. Lorem Ipsum has Lorem Ipsum is simply dummy text of the printing and typesetting industry. Lorem Ipsum has Lorem Ipsum is simply dummy text of the printing and typesetting industry. Lorem Ipsum has Lorem Ipsum is simply dummy text of the printing and typesetting industry. Lorem Ipsum has Lorem Ipsum is simply dummy text of the printing and typesetting industry. Lorem Ipsum has Lorem Ipsum is simply dummy text of the printing and typesetting industry. Lorem Ipsum has Lorem Ipsum is simply dummy text of the printing and typesetting industry. Lorem Ipsum has</p>
  <div class="photo photo-paper" role="img" aria-label="Pen resting on a newspaper funds listing"></div>
  <div class="verified">Verified and Protected by</div>
  <svg class="badge" style="left:177px;top:551px" width="80" height="30" viewBox="0 0 80 30" role="img" aria-label="Security certificate badge"><rect width="80" height="30" rx="4" fill="var(--badge)"/></svg>
  <svg class="badge" style="left:336px;top:551px" width="76" height="30" viewBox="0 0 76 30" role="img" aria-label="Audit partner badge"><rect width="76" height="30" rx="4" fill="var(--badge)"/></svg>
  <svg class="badge" style="left:500px;top:551px" width="90" height="30" viewBox="0 0 90 30" role="img" aria-label="Privacy certificate badge"><rect width="90" height="30" rx="4" fill="var(--badge)"/></svg>
  <svg class="badge" style="left:643px;top:546px" width="40" height="40" viewBox="0 0 40 40" role="img" aria-label="Trust seal badge"><circle cx="20" cy="20" r="20" fill="var(--badge)"/></svg>
</main>

<footer class="footer">
  <div class="footer-col" style="left:95px"><h3>ABOUT US</h3><ul><li>History</li><li>Expertize</li><li>Identity</li><li>Strategy</li><li>Contact us</li></ul></div>
  <div class="footer-col" style="left:213px"><h3>INVESTMENT</h3><ul><li>Term Deposit</li><li>Management &amp; Strategy</li><li>Cleints Relaions</li><li>Tax Advice</li><li>Active Advisory Group</li><li>Management Slection Serive</li><li>Private Equity</li><li>Wealth Analysis</li></ul></div>
  <div class="footer-col" style="left:400px"><h3>FUNDS</h3><ul><li>Term Deposit</li><li>Management &amp; Strategy</li><li>Cleints Relaions</li><li>Tax Advice</li><li>Active Advisory Group</li><li>Management Slection Serive</li><li>Private Equity</li><li>Wealth Analysis</li></ul></div>
  <div class="footer-col" style="left:605px"><h3>CURRENCY EXCHANGE</h3><ul><li>Term Deposit</li><li>Management &amp; Strategy</li><li>Cleints Relaions</li><li>Tax Advice</li><li>Active Advisory Group</li><li>Management Slection Serive</li><li>Private Equity</li><li>Wealth Analysis</li></ul></div>
  <div class="footer-col" style="left:824px"><h3>BROKERAGE</h3><ul><li>Term Deposit</li><li>Management &amp; Strategy</li><li>Cleints Relaions</li><li>Tax Advice</li><li>Active Advisory Group</li><li>Management Slection Serive</li><li>Private Equity</li><li>Wealth Analysis</li></ul></div>
</footer>
<div class="bottom-bar"></div>
</body>
</html>
```